Baby Store - GIF Banner

About the Company:
Nalifa.com.sa is an online shop for baby related products in Saudi Arabia. The targeted audience is moms between 25-35 years of age. The word "Nalifa" means Shop/Store in the Arabic Language.
About the Banner:
The banners should be designed in animated GIF format and provide in four sizes, upon clicking on the banner it will take you to Nalifa website. The Banners will convey the following:
- All your baby daily needs
مستلزمات طفلك اليومية من نليفا
- Free same day delivery
توصيل مجاني بنفس اليوم في الرياض
- Subscribe now for special discounts.
سجلي الان لتحصلي على خصم خاص
Note: Arabic Text are attached in PSD format.
Design Requirements:
Company Logo is attached.
Sample of product photos will be provided.
Baby photo can be used.
Shop Now Button should be included in the design.
تسوق الان
Shop Now
Logo colors are the main colors to be used (Blue, Pink, Gray)
DropBox Link: will be provided upon request.
Design Style:
- Play full
- Feminine
- Creative
Delivery Requirements:
Initially we may start working on an English version, at the end you will must to provide an Arabic version of the Banners in addition to the English version. Arabic translations are provided above, Note that Arabic language is from right to left opposite to the English language.
Banners Sizes Required:
Banner 1: 728 x 90
Banner 2: 480 x 70
Banner 3: 300 x 250
Banner 4: 648x40
Banner Specs:
Size less than 100 kb
Background less than 80% alpha
Please pay EXTRA attention to the guidelines in the following link:
https://help.brivantomedia.net/clips/answer/530418
If you have any questions please let me know, wish you the best of luck.
Modern Moms of age 25-35.
Shop

```html
<!DOCTYPE html>
<html lang="ar">
<head>
<meta charset="utf-8">
<title>Nalifa Banner</title>
<link rel="stylesheet" href="https://fonts.googleapis.com/css2?family=Lalezar&display=swap">
<style>
  :root {
    --sky-top: #a6d3f5;
    --sky-bottom: #c9e6fb;
    --cloud: #ffffff;
    --cloud-soft: rgba(255, 255, 255, 0);
    --brand-blue: #1f8fd8;
    --brand-pink: #f06fa4;
    --cta-blue: #7cc3ee;
    --headline: #ffffff;
    --headline-edge: #1b64a8;
    --frame: #cfd6dc;
  }
  html, body {
    margin: 0;
    padding: 0;
    overflow: hidden;
    background: #ffffff;
  }
  .banner {
    position: relative;
    width: 1200px;
    height: 148px;
    box-sizing: border-box;
    border: 2px solid var(--frame);
    background: linear-gradient(180deg, var(--sky-top) 0%, var(--sky-bottom) 100%);
    overflow: hidden;
    font-family: "Lalezar", sans-serif;
  }
  .banner__cloud-area {
    position: absolute;
    left: 0;
    top: 0;
    width: 340px;
    height: 144px;
    background: linear-gradient(90deg, var(--cloud) 0%, var(--cloud) 72%, var(--cloud-soft) 100%);
    border-radius: 0 70px 70px 0;
  }
  .brand {
    position: absolute;
    left: 30px;
    top: 14px;
    margin: 0;
    display: flex;
    align-items: center;
    gap: 10px;
    font-size: 40px;
    line-height: 1;
    color: var(--brand-blue);
    direction: ltr;
  }
  .brand__dot {
    width: 18px;
    height: 18px;
    border-radius: 50%;
    background: var(--brand-pink);
  }
  .cta {
    position: absolute;
    left: 60px;
    top: 84px;
    padding: 8px 26px 4px;
    font-size: 34px;
    line-height: 1;
    color: var(--cta-blue);
    background: var(--cloud);
    border: 2px solid var(--cta-blue);
    border-radius: 30px;
    text-decoration: none;
  }
  .headline {
    position: absolute;
    right: 20px;
    top: 10px;
    margin: 0;
    font-size: 56px;
    line-height: 1.1;
    font-weight: 400;
    color: var(--headline);
    text-shadow:
      -2px -2px 0 var(--headline-edge), 2px -2px 0 var(--headline-edge),
      -2px 2px 0 var(--headline-edge), 2px 2px 0 var(--headline-edge),
      0 3px 0 var(--headline-edge), 3px 4px 2px rgba(20, 70, 120, 0.45);
    direction: rtl;
  }
</style>
</head>
<body>
  <div class="banner">
    <div class="banner__cloud-area" role="img" aria-label="Soft white clouds illustration"></div>

    <p class="brand"><span>Nalifa.com.sa</span><span class="brand__dot"></span></p>
    <a class="cta" href="https://nalifa.com.sa" dir="rtl">تسوق الان</a>

    <h1 class="headline">مستلزمات طفلك اليومية من نليفا</h1>
  </div>
</body>
</html>
```